Sign Design

We already have a logo, but would like to design 2 x signs.
Sign 1:
Dimensions 1500mm wide x 2500m high.
Information to include on sign: - Clinic name and logo (attached)
- the word "DENTIST "
- Street number (which is 847)
Phone number (which is 6154 3970)

Sign 2:
Dimensions: 800mm wide x 600mm high

```html
<!DOCTYPE html>
<html lang="en">
<head>
<meta charset="utf-8">
<title>Kellbrook Dental Care – Signage</title>
<link rel="stylesheet" href="https://fonts.googleapis.com/css2?family=Arimo:wght@400;700&display=swap">
<style>
  :root {
    --backdrop: #3a3939;
    --backdrop-dark: #1e1e1f;
    --green-dark: #0f7a3c;
    --green-mid: #22a33a;
    --green-light: #9bd84a;
    --green-pale: #e6f6cc;
    --ink: #333333;
    --white: #ffffff;
  }
  * { box-sizing: border-box; margin: 0; padding: 0; }
  html, body { width: 1200px; height: 960px; overflow: hidden; }
  body {
    position: relative;
    background: radial-gradient(ellipse at 45% 45%, var(--backdrop) 0%, var(--backdrop-dark) 80%);
    font-family: "Arimo", Arial, sans-serif;
  }

  /* Sign 1: fascia banner */
  .fascia {
    position: absolute;
    left: 54px; top: 169px;
    width: 1092px; height: 182px;
    background: linear-gradient(90deg, var(--white) 0%, var(--white) 15%, var(--green-pale) 100%);
    overflow: hidden;
  }
  .fascia .art { position: absolute; inset: 0; }
  .fascia .brand-mark {
    position: absolute; left: 60px; top: 52px;
    width: 58px; height: 58px; border-radius: 50%;
    background: var(--green-mid);
  }
  .fascia .brand-name {
    position: absolute; left: 184px; top: 36px;
    color: var(--green-dark); font-weight: 400; line-height: 1;
    letter-spacing: -2px;
  }
  .fascia .brand-name .line-1 { display: block; font-size: 52px; }
  .fascia .brand-name .line-2 { display: block; font-size: 28px; margin: 6px 0 0 126px; letter-spacing: -1px; }
  .fascia .service {
    position: absolute; left: 606px; top: 20px;
    font-size: 46px; font-weight: 400; color: var(--green-light);
    letter-spacing: -1px;
  }
  .fascia .contact {
    position: absolute; left: 180px; top: 148px;
    display: flex; gap: 38px; align-items: baseline;
    font-size: 16px; color: var(--ink);
  }
  .fascia .contact strong {
    font-size: 22px; color: var(--green-dark); font-weight: 700; margin-left: 12px;
  }

  /* Sign 2: panel */
  .panel {
    position: absolute;
    left: 309px; top: 428px;
    width: 582px; height: 437px;
    background: var(--white);
    overflow: hidden;
  }
  .panel .art { position: absolute; inset: 0; }
  .panel .brand-mark {
    position: absolute; left: 130px; top: 60px;
    width: 80px; height: 80px; border-radius: 50%;
    background: var(--green-mid);
  }
  .panel .brand-name {
    position: absolute; left: 34px; top: 166px;
    color: var(--green-dark); font-weight: 400; line-height: 1;
    letter-spacing: -2px;
  }
  .panel .brand-name .line-1 { display: block; font-size: 52px; }
  .panel .brand-name .line-2 { display: block; font-size: 28px; margin: 4px 0 0 88px; letter-spacing: -1px; }
</style>
</head>
<body>

<section class="fascia" aria-label="Fascia sign">
  <svg class="art" viewBox="0 0 1092 182" width="1092" height="182">
    <defs>
      <linearGradient id="fascia-couple" x1="0" y1="0" x2="1" y2="1">
        <stop offset="0" stop-color="#6b4a36"/><stop offset=".45" stop-color="#e3b79a"/><stop offset="1" stop-color="#f4e8e2"/>
      </linearGradient>
      <linearGradient id="fascia-chair" x1="0" y1="0" x2="1" y2="1">
        <stop offset="0" stop-color="#3f9ad6"/><stop offset=".6" stop-color="#d7a58a"/><stop offset="1" stop-color="#eef2f6"/>
      </linearGradient>
      <linearGradient id="fascia-exam" x1="0" y1="0" x2="1" y2="1">
        <stop offset="0" stop-color="#e8e6e4"/><stop offset=".5" stop-color="#e2b39b"/><stop offset="1" stop-color="#7ab8e0"/>
      </linearGradient>
    </defs>
    <path class="swoosh" d="M700 182 Q 900 150 1092 118 L1092 182 Z" fill="var(--green-light)"/>
    <g class="photo photo-couple" role="img" aria-label="Photo of a smiling young couple">
      <circle cx="980" cy="84" r="116" fill="var(--green-dark)"/>
      <circle cx="980" cy="84" r="110" fill="var(--white)"/>
      <circle cx="980" cy="84" r="106" fill="var(--green-light)"/>
      <circle cx="980" cy="84" r="102" fill="url(#fascia-couple)"/>
    </g>
    <g class="photo photo-chair" role="img" aria-label="Photo of a man having a dental check-up">
      <circle cx="848" cy="118" r="72" fill="var(--green-dark)"/>
      <circle cx="848" cy="118" r="67" fill="var(--white)"/>
      <circle cx="848" cy="118" r="64" fill="url(#fascia-chair)"/>
    </g>
    <g class="photo photo-exam" role="img" aria-label="Photo of a woman having her teeth examined">
      <circle cx="726" cy="130" r="61" fill="var(--green-dark)"/>
      <circle cx="726" cy="130" r="56" fill="var(--white)"/>
      <circle cx="726" cy="130" r="53" fill="url(#fascia-exam)"/>
    </g>
  </svg>
  <span class="brand-mark" aria-hidden="true"></span>
  <h1 class="brand-name"><span class="line-1">Kellbrook</span><span class="line-2">Dental Care</span></h1>
  <p class="service">DENTIST</p>
  <p class="contact">
    <span>Street number<strong>847</strong></span>
    <span>Phone number<strong>6154 3970</strong></span>
  </p>
</section>

<section class="panel" aria-label="Panel sign">
  <svg class="art" viewBox="0 0 582 437" width="582" height="437">
    <defs>
      <linearGradient id="panel-couple" x1="0" y1="0" x2="1" y2="1">
        <stop offset="0" stop-color="#5a3d2c"/><stop offset=".4" stop-color="#e2b597"/><stop offset="1" stop-color="#f6ece6"/>
      </linearGradient>
      <linearGradient id="panel-chair" x1="0" y1="0" x2="1" y2="1">
        <stop offset="0" stop-color="#3d98d6"/><stop offset=".6" stop-color="#d9a68b"/><stop offset="1" stop-color="#eef2f6"/>
      </linearGradient>
      <linearGradient id="panel-exam" x1="0" y1="0" x2="1" y2="1">
        <stop offset="0" stop-color="#e9e7e5"/><stop offset=".5" stop-color="#e3b49c"/><stop offset="1" stop-color="#6fb2de"/>
      </linearGradient>
    </defs>
    <path class="swoosh-pale" d="M0 392 Q 300 350 582 300 L582 437 L0 437 Z" fill="var(--green-pale)"/>
    <path class="swoosh" d="M0 404 Q 300 372 582 318 L582 437 L0 437 Z" fill="var(--green-light)"/>
    <g class="photo photo-couple" role="img" aria-label="Photo of a smiling young couple">
      <circle cx="492" cy="138" r="176" fill="var(--green-dark)"/>
      <circle cx="492" cy="138" r="168" fill="var(--white)"/>
      <circle cx="492" cy="138" r="164" fill="var(--green-light)"/>
      <circle cx="492" cy="138" r="159" fill="url(#panel-couple)"/>
    </g>
    <g class="photo photo-chair" role="img" aria-label="Photo of a man having a dental check-up">
      <circle cx="366" cy="316" r="118" fill="var(--green-dark)"/>
      <circle cx="366" cy="316" r="111" fill="var(--white)"/>
      <circle cx="366" cy="316" r="107" fill="var(--green-light)"/>
      <circle cx="366" cy="316" r="103" fill="url(#panel-chair)"/>
    </g>
    <g class="photo photo-exam" role="img" aria-label="Photo of a woman having her teeth examined">
      <circle cx="183" cy="350" r="88" fill="var(--green-dark)"/>
      <circle cx="183" cy="350" r="82" fill="var(--white)"/>
      <circle cx="183" cy="350" r="79" fill="var(--green-light)"/>
      <circle cx="183" cy="350" r="75" fill="url(#panel-exam)"/>
    </g>
  </svg>
  <span class="brand-mark" aria-hidden="true"></span>
  <h2 class="brand-name"><span class="line-1">Kellbrook</span><span class="line-2">Dental Care</span></h2>
</section>

</body>
</html>
```